Neighbor of existing customer door hanger

We are a landscaping services company (Pest Control & Lawn Fertilization). I am looking for a piece that my sales people can leave behind at the neighbors of our current customers offering our services to them.

I'm not a graphics guy, not even close, I started making a sample that is not any good, but it might give the general idea. I have attached that design here. There is a template available from the printer for 4.25 x 11". I have included that as well

Target Market(s)

Women homeowners 35-50

Industry/Entity Type

Landscape Gardening

Font styles to use
Sans Serif

Colors

Designer to choose colors to be used in the design.

Requirements
Must have
• we are looking for a space to write the name or address of our customer, include 2 specials ( 1 for pest control, 1 for Lawn fertilization and weed control) that make the neighbors feel like they are getting a deal because they are neighbors of our customer.
• the back side of the postcard will list our range of services and have a space for the salesman to write his name.
• This will be printed on a glossy cardstock (unless the designer suggests something else).
• Phone numbers, Website, logos

```html
<!DOCTYPE html>
<html lang="en">
<head>
<meta charset="utf-8">
<title>Fernway Door Hanger</title>
<link href="https://fonts.googleapis.com/css2?family=Open+Sans:wght@400;600;700;800&display=swap" rel="stylesheet">
<style>
:root{
  --green:#127a2f;
  --green-dark:#0b6424;
  --lime:#8cc63f;
  --ink:#1d1d1d;
  --char:#2b2b2b;
  --white:#ffffff;
  --stage:#b9b9b9;
  --red:#d9262b;
}
*{margin:0;padding:0;box-sizing:border-box}
html,body{width:1200px;height:1200px;overflow:hidden}
body{background:var(--stage);font-family:"Open Sans",sans-serif;position:relative}
.hanger{position:absolute;top:51px;width:422px;height:1098px;overflow:hidden;background:var(--white)}
.hanger--front{left:130px}
.hanger--back{left:631px;background:var(--char)}
.hanger__art{position:absolute;inset:0;width:422px;height:1098px}
.t{position:absolute;white-space:nowrap}
.center{left:0;right:0;text-align:center}

/* front */
.brand{left:26px;top:486px;font-size:34px;line-height:34px;font-weight:700;color:var(--green);letter-spacing:1px;display:flex;align-items:center;gap:10px}
.brand__dot{width:14px;height:14px;border-radius:50%;background:var(--lime)}
.brand-tag{left:29px;top:525px;font-size:7.5px;line-height:9px;color:#555;letter-spacing:.2px}
.headline{top:546px;font-size:49px;font-weight:800;color:var(--green);letter-spacing:-.5px}
.subhead{top:603px;font-size:19px;font-weight:600;color:var(--green)}
.write-box{position:absolute;left:25px;top:643px;width:372px;height:27px;border:1px solid #bbb;border-radius:6px}
.body{font-size:15.5px;font-weight:700;color:var(--ink);line-height:19px}
.band{position:absolute;left:0;width:422px;top:789px;height:33px;background:var(--green);color:var(--white);font-size:20px;font-weight:700;text-align:center;line-height:33px}
.special-1{top:825px;font-size:26px;font-weight:700;color:var(--green)}
.special-2{position:absolute;left:62px;top:875px;width:298px;height:36px;background:var(--lime);color:var(--ink);font-size:28px;font-weight:700;text-align:center;line-height:36px}
.perk{font-size:17px;line-height:22px;font-weight:700;color:var(--ink);display:flex;align-items:center;gap:10px}
.tick{width:9px;height:9px;flex:none}
.foot{color:var(--white);display:flex;align-items:center}
.foot__phone{font-weight:700}
.foot__web{font-size:15px}
.foot__web b{color:var(--lime);font-weight:600}

/* back */
.title-band{position:absolute;left:42px;top:394px;width:336px;height:36px;background:var(--green);color:var(--white);font-size:25px;font-weight:700;text-align:center;line-height:36px}
.svc{font-size:18px;color:var(--white);line-height:22.5px;display:flex;gap:14px}
.svc .tick{margin-top:7px}
.coupon{position:absolute;left:26px;top:813px;width:369px;height:160px}
.coupon svg{position:absolute;inset:0}
.coupon__label{position:absolute;left:5px;top:64px;width:70px;transform:rotate(-90deg);color:var(--white);font-size:18px;font-weight:700;letter-spacing:1px;text-align:center}
.coupon__cost{left:150px;top:6px;font-size:31px;line-height:40px;color:var(--ink)}
.coupon__price{left:88px;top:42px;font-size:68px;line-height:62px;font-weight:800;color:var(--white);letter-spacing:-1px}
.coupon__bug{position:absolute;left:286px;top:40px;width:54px;height:72px;border-radius:50%;background:var(--red)}
.coupon__first{left:89px;top:108px;font-size:12px;line-height:14px;font-weight:700;color:var(--ink)}
.coupon__quote{left:89px;top:125px;font-size:14.5px;font-weight:700;color:var(--ink);line-height:15px}
.back-phone{left:0;width:207px;text-align:center;top:1039px;font-size:28px;font-weight:700;color:var(--white)}
.back-web{left:207px;width:215px;text-align:center;top:1047px;font-size:15px;color:var(--white)}
.back-web b{color:var(--lime);font-weight:600}
</style>
</head>
<body>

<!-- FRONT -->
<section class="hanger hanger--front">
  <svg class="hanger__art" viewBox="0 0 422 1098">
    <defs>
      <linearGradient id="frontPhoto" x1="0" y1="0" x2="0" y2="1">
        <stop offset="0" stop-color="#5f7584"/>
        <stop offset=".4" stop-color="#7a6a45"/>
        <stop offset=".75" stop-color="#5b6a2e"/>
        <stop offset="1" stop-color="#3f6a22"/>
      </linearGradient>
    </defs>
    <path role="img" aria-label="Photo of a landscaped front yard with stone walls, shrubs and garden lights" d="M0 0H422V310C380 420 250 455 0 465Z" fill="url(#frontPhoto)"/>
    <path d="M0 465C250 455 380 420 422 310V350C380 455 240 495 0 490Z" fill="var(--green)"/>
    <path d="M0 490C240 495 380 455 422 350V372C380 480 240 510 0 485C0 488 0 492 0 495Z" fill="var(--lime)"/>
    <circle cx="211" cy="135" r="66" fill="var(--white)"/>
    <path d="M0 1020C200 985 410 995 422 915V1098H0Z" fill="var(--lime)"/>
    <path d="M0 1032C200 1000 410 1010 422 932V1098H0Z" fill="var(--green)"/>
    <path d="M0 1050C200 1022 410 1030 422 955V1098H0Z" fill="var(--char)"/>
    <line x1="194" y1="1052" x2="194" y2="1086" stroke="var(--white)" stroke-width="1"/>
    <circle cx="28" cy="1069" r="8" fill="var(--white)"/>
    <circle cx="224" cy="1069" r="8" fill="none" stroke="var(--white)" stroke-width="1.5"/>
    <path d="M216 1069H232M224 1061V1077" stroke="var(--white)" stroke-width="1.2"/>
    <path d="M24 1065q1 7 8 8l1.5-2-2.5-2-1.5 1q-2-1-3-3l1-1.5-2-2.5z" fill="var(--char)"/>
  </svg>

  <div class="t brand">Fernway<span class="brand__dot"></span></div>
  <div class="t brand-tag">LAWN FERTILIZATION | PEST CONTROL | LANDSCAPING</div>
  <div class="t center headline">HEY NEIGHBOR</div>
  <div class="t center subhead">We service your Friends</div>
  <div class="write-box"></div>
  <div class="t center body" style="top:685px">Because your friends use our services, You<br>get Neighborhood discounts!</div>
  <div class="t center body" style="top:734px">Family owned &amp; operated in Salt Lake City<br>for over 25 years</div>
  <div class="band">Neighborhood Discounts on:</div>
  <div class="t center special-1">Full Service Pest Control</div>
  <div class="special-2">Lawn Fertilization</div>
  <div class="t perk" style="left:37px;top:924px"><svg class="tick" viewBox="0 0 10 10"><circle cx="5" cy="5" r="5" fill="var(--green)"/><path d="M2.8 5.2l1.6 1.5 3-3" stroke="#fff" stroke-width="1.3" fill="none"/></svg>DISEASE CONTROL</div>
  <div class="t perk" style="left:258px;top:924px"><svg class="tick" viewBox="0 0 10 10"><circle cx="5" cy="5" r="5" fill="var(--green)"/><path d="M2.8 5.2l1.6 1.5 3-3" stroke="#fff" stroke-width="1.3" fill="none"/></svg>GETTING RID</div>
  <div class="t perk" style="left:37px;top:952px"><svg class="tick" viewBox="0 0 10 10"><circle cx="5" cy="5" r="5" fill="var(--green)"/><path d="M2.8 5.2l1.6 1.5 3-3" stroke="#fff" stroke-width="1.3" fill="none"/></svg>BALANCED NUTRITION</div>
  <div class="t foot foot__phone" style="left:44px;top:1054px;font-size:22px">555-014-2290</div>
  <div class="t foot foot__web" style="left:236px;top:1059px">www.<b>GETFERNWAY</b>.com</div>
</section>

<!-- BACK -->
<section class="hanger hanger--back">
  <svg class="hanger__art" viewBox="0 0 422 1098">
    <defs>
      <linearGradient id="backPhoto" x1="0" y1="0" x2="0" y2="1">
        <stop offset="0" stop-color="#7d6a45"/>
        <stop offset=".35" stop-color="#8a5a34"/>
        <stop offset=".55" stop-color="#5f9a35"/>
        <stop offset="1" stop-color="#3f8a26"/>
      </linearGradient>
    </defs>
    <path role="img" aria-label="Photo of a green lawn with steel retaining wall planters" d="M0 0H422V150C380 300 200 335 0 385Z" fill="url(#backPhoto)"/>
    <path d="M0 385C200 335 380 300 422 150V185C380 330 220 355 0 410Z" fill="var(--green)"/>
    <path d="M0 410C220 355 380 330 422 185V200C380 345 220 372 0 430Z" fill="var(--lime)"/>
    <circle cx="211" cy="135" r="66" fill="var(--white)"/>
    <line x1="207" y1="1005" x2="207" y2="1069" stroke="var(--white)" stroke-width="1"/>
    <circle cx="106" cy="1022" r="12" fill="var(--white)"/>
    <path d="M100 1016q1.5 10 11 11.5l2-3-3.5-2.5-2 1.5q-3-1.5-4.5-4.5l1.5-2-2.5-3.5z" fill="var(--char)"/>
    <circle cx="313" cy="1025" r="11" fill="var(--white)"/>
    <circle cx="313" cy="1025" r="7" fill="none" stroke="var(--char)" stroke-width="1.2"/>
    <path d="M306 1025H320M313 1018V1032M308 1021H318M308 1029H318" stroke="var(--char)" stroke-width="1"/>
  </svg>

  <div class="title-band">Full Service Pest Control</div>

  <div class="t svc" style="left:26px;top:447px"><svg class="tick" viewBox="0 0 10 10"><circle cx="5" cy="5" r="5" fill="#fff"/><path d="M2.8 5.2l1.6 1.5 3-3" stroke="var(--char)" stroke-width="1.3" fill="none"/></svg><span>Inside &amp; Out<br>&nbsp;Treatments</span></div>
  <div class="t svc" style="left:26px;top:499px"><svg class="tick" viewBox="0 0 10 10"><circle cx="5" cy="5" r="5" fill="#fff"/><path d="M2.8 5.2l1.6 1.5 3-3" stroke="var(--char)" stroke-width="1.3" fill="none"/></svg><span>Wasps/Hornets</span></div>
  <div class="t svc" style="left:26px;top:532px"><svg class="tick" viewBox="0 0 10 10"><circle cx="5" cy="5" r="5" fill="#fff"/><path d="M2.8 5.2l1.6 1.5 3-3" stroke="var(--char)" stroke-width="1.3" fill="none"/></svg><span>Mice/Rats</span></div>
  <div class="t svc" style="left:26px;top:564px"><svg class="tick" viewBox="0 0 10 10"><circle cx="5" cy="5" r="5" fill="#fff"/><path d="M2.8 5.2l1.6 1.5 3-3" stroke="var(--char)" stroke-width="1.3" fill="none"/></svg><span>Gophers/Voles</span></div>
  <div class="t svc" style="left:26px;top:598px"><svg class="tick" viewBox="0 0 10 10"><circle cx="5" cy="5" r="5" fill="#fff"/><path d="M2.8 5.2l1.6 1.5 3-3" stroke="var(--char)" stroke-width="1.3" fill="none"/></svg><span>Lawn Fertilization<br>&amp; Weed Control</span></div>
  <div class="t svc" style="left:26px;top:651px"><svg class="tick" viewBox="0 0 10 10"><circle cx="5" cy="5" r="5" fill="#fff"/><path d="M2.8 5.2l1.6 1.5 3-3" stroke="var(--char)" stroke-width="1.3" fill="none"/></svg><span>Sprinkler Repairs<br>&amp; Installation</span></div>
  <div class="t svc" style="left:26px;top:704px"><svg class="tick" viewBox="0 0 10 10"><circle cx="5" cy="5" r="5" fill="#fff"/><path d="M2.8 5.2l1.6 1.5 3-3" stroke="var(--char)" stroke-width="1.3" fill="none"/></svg><span>Wiring</span></div>
  <div class="t svc" style="left:26px;top:737px"><svg class="tick" viewBox="0 0 10 10"><circle cx="5" cy="5" r="5" fill="#fff"/><path d="M2.8 5.2l1.6 1.5 3-3" stroke="var(--char)" stroke-width="1.3" fill="none"/></svg><span>Xeriscape/Drip<br>Conversion</span></div>

  <div class="t svc" style="left:219px;top:447px"><svg class="tick" viewBox="0 0 10 10"><circle cx="5" cy="5" r="5" fill="#fff"/><path d="M2.8 5.2l1.6 1.5 3-3" stroke="var(--char)" stroke-width="1.3" fill="none"/></svg><span>Landscape Design<br>&amp; Install</span></div>
  <div class="t svc" style="left:219px;top:500px"><svg class="tick" viewBox="0 0 10 10"><circle cx="5" cy="5" r="5" fill="#fff"/><path d="M2.8 5.2l1.6 1.5 3-3" stroke="var(--char)" stroke-width="1.3" fill="none"/></svg><span>Pavers</span></div>
  <div class="t svc" style="left:219px;top:532px"><svg class="tick" viewBox="0 0 10 10"><circle cx="5" cy="5" r="5" fill="#fff"/><path d="M2.8 5.2l1.6 1.5 3-3" stroke="var(--char)" stroke-width="1.3" fill="none"/></svg><span>Pergolas/Pavilions</span></div>
  <div class="t svc" style="left:219px;top:567px"><svg class="tick" viewBox="0 0 10 10"><circle cx="5" cy="5" r="5" fill="#fff"/><path d="M2.8 5.2l1.6 1.5 3-3" stroke="var(--char)" stroke-width="1.3" fill="none"/></svg><span>Retaining walls</span></div>
  <div class="t svc" style="left:219px;top:603px"><svg class="tick" viewBox="0 0 10 10"><circle cx="5" cy="5" r="5" fill="#fff"/><path d="M2.8 5.2l1.6 1.5 3-3" stroke="var(--char)" stroke-width="1.3" fill="none"/></svg><span>Steel retaining</span></div>
  <div class="t svc" style="left:219px;top:638px"><svg class="tick" viewBox="0 0 10 10"><circle cx="5" cy="5" r="5" fill="#fff"/><path d="M2.8 5.2l1.6 1.5 3-3" stroke="var(--char)" stroke-width="1.3" fill="none"/></svg><span>Water features</span></div>
  <div class="t svc" style="left:219px;top:670px"><svg class="tick" viewBox="0 0 10 10"><circle cx="5" cy="5" r="5" fill="#fff"/><path d="M2.8 5.2l1.6 1.5 3-3" stroke="var(--char)" stroke-width="1.3" fill="none"/></svg><span>Landscape Lighting</span></div>
  <div class="t svc" style="left:219px;top:705px"><svg class="tick" viewBox="0 0 10 10"><circle cx="5" cy="5" r="5" fill="#fff"/><path d="M2.8 5.2l1.6 1.5 3-3" stroke="var(--char)" stroke-width="1.3" fill="none"/></svg><span>Fire features</span></div>

  <div class="coupon">
    <svg viewBox="0 0 369 160">
      <path d="M6 0H369V60a18 18 0 0 0 0 40V160H6a6 6 0 0 1-6-6V6a6 6 0 0 1 6-6Z" fill="var(--lime)"/>
      <path d="M6 0H72V160H6a6 6 0 0 1-6-6V6a6 6 0 0 1 6-6Z" fill="var(--green)"/>
      <circle cx="72" cy="0" r="10" fill="var(--char)"/>
      <circle cx="72" cy="160" r="10" fill="var(--char)"/>
      <line x1="72" y1="14" x2="72" y2="146" stroke="var(--char)" stroke-width="2.5" stroke-dasharray="1 18" stroke-linecap="round"/>
    </svg>
    <div class="coupon__label">COUPON</div>
    <div class="t coupon__cost">YOUR COST</div>
    <div class="t coupon__price">$9.95</div>
    <div class="coupon__bug" role="img" aria-label="Cartoon red beetle illustration"></div>
    <div class="t coupon__first">First Service</div>
    <div class="t coupon__quote">“You won't see a bug or we re-treat<br>for Free"</div>
  </div>

  <div class="t back-phone">555-014-2290</div>
  <div class="t back-web">www.<b>GETFERNWAY</b>.com</div>
</section>

</body>
</html>
```